One label design for 3 different sizes of honey bottles

Our honey company -- Amber Hollow Apiary -- needs new product labels, integrating our new name and logo. We would like one label design that presents equally well on three different sizes of plastic honey bottles. Designs should include a front and back label.

Keep in mind that we really like our old label. Please submit designs that have a similar color and font scheme as the old label.

In the uploaded files, you will find (1) detailed content instructions for each size label (2 lb, 1 lb, 8 oz), (2) photo of three plastic bottles without labels, (3) *.ai file for the new company logo, and (4) image of old package label.

Requirements
Must have
• Same look and feel as our old label, but with our new name and logo

```html
<!DOCTYPE html>
<html lang="en">
<head>
<meta charset="utf-8">
<title>Amber Hollow Apiary – Honey Labels</title>
<link rel="stylesheet" href="https://fonts.googleapis.com/css2?family=Barlow:wght@400;500;700&family=Josefin+Sans:wght@300&family=Rye&display=swap">
<style>
  :root {
    --paper: #f8f6e6;
    --ink: #3e3e36;
    --bloom: #cfcfc6;
    --bloom-light: #ecebdf;
    --panel: #ffffff;
    --backdrop: #ffffff;
  }
  * { margin: 0; padding: 0; box-sizing: border-box; }
  html, body { width: 1200px; height: 894px; overflow: hidden; background: var(--backdrop); }
  .sheet { position: relative; width: 1200px; height: 894px; }

  .label { position: absolute; top: 0; height: 894px; color: var(--ink); }
  .label--front { left: 0; width: 596px; }
  .label--back { left: 632px; width: 568px; }
  .label-shape { position: absolute; inset: 0; width: 100%; height: 100%; }

  .centered { position: absolute; left: 0; width: 100%; text-align: center; }

  .bloom {
    position: absolute; border-radius: 50%;
    background: radial-gradient(circle at 50% 50%, var(--bloom-light) 0 10%, var(--bloom) 30%, rgba(207,207,198,0.6) 60%, rgba(207,207,198,0) 72%);
  }
  .ornament {
    position: absolute; border-radius: 30% 30% 40% 40%;
    background: radial-gradient(circle, rgba(62,62,54,0.55), rgba(62,62,54,0.25) 70%, rgba(62,62,54,0) 100%);
  }

  /* shared brand mark stand-in */
  .brand-circle { position: absolute; border: 2px solid var(--ink); border-radius: 50%; }
  .brand-name { font-family: "Barlow", sans-serif; font-weight: 500; color: var(--ink); }

  /* front */
  .tagline { font-family: "Josefin Sans", sans-serif; font-weight: 300; letter-spacing: 1px; }
  .front-tagline { top: 70px; font-size: 35px; }
  .rule { position: absolute; height: 2px; background: var(--ink); }
  .wordmark { font-family: "Rye", serif; color: var(--ink); letter-spacing: 2px; }
  .front-wordmark { top: 160px; font-size: 118px; line-height: 1.2; }
  .front-circle { left: 258px; top: 372px; width: 80px; height: 80px; }
  .front-brand { top: 478px; font-size: 48px; line-height: 56px; }
  .net-weight { font-family: "Barlow", sans-serif; font-weight: 500; }
  .front-net { top: 690px; font-size: 33px; line-height: 48px; letter-spacing: 1px; }

  /* back */
  .back-circle { left: 137px; top: 52px; width: 46px; height: 46px; }
  .back-brand { position: absolute; left: 70px; top: 106px; width: 180px; font-size: 21px; line-height: 24px; text-align: center; }
  .back-wordmark { position: absolute; left: 300px; top: 46px; width: 220px; text-align: center; font-size: 56px; line-height: 1.2; }
  .back-tagline { position: absolute; left: 300px; top: 120px; width: 220px; text-align: center; font-size: 16px; }
  .promise {
    top: 196px; font-family: "Barlow", sans-serif; font-weight: 700;
    font-size: 21.5px; line-height: 30px; white-space: nowrap;
  }
  .ingredients-title { top: 356px; font-family: "Barlow", sans-serif; font-weight: 700; font-size: 37px; letter-spacing: 1px; }
  .nutrition {
    position: absolute; left: 58px; top: 406px; width: 456px; height: 191px;
    background: var(--panel); text-align: center; white-space: nowrap;
    font-family: "Barlow", sans-serif; font-size: 12px; line-height: 19px; padding: 4px 6px 0;
  }
  .nutrition strong { font-weight: 700; font-size: 13px; }
  .nutrition .lead { font-size: 16px; }
  .nutrition .big { font-size: 17px; }
  .nutrition .note { margin-top: 12px; line-height: 17px; }
  .infant-warning { top: 618px; font-family: "Barlow", sans-serif; font-weight: 700; font-size: 11px; }
  .address {
    top: 660px; font-family: "Barlow", sans-serif; font-weight: 700;
    font-size: 19.5px; line-height: 25.5px; font-style: normal;
  }
  .back-net { top: 797px; font-size: 14px; line-height: 21px; }
</style>
</head>
<body>
<main class="sheet">

  <section class="label label--front">
    <svg class="label-shape" viewBox="0 0 596 894" aria-hidden="true">
      <path d="M58,2 H538 L556,20 V134 H594 V752 H556 V874 L538,892 H58 L40,874 V752 H2 V134 H40 V20 Z" fill="var(--paper)" stroke="var(--ink)" stroke-width="1"/>
      <path d="M70,22 H526 L540,36 V150 H534 V340 M534,740 V862 L522,874 H74 L56,862 V740 M56,340 V150 H50 V36 Z" fill="none" stroke="var(--ink)" stroke-width="1.2"/>
    </svg>
    <div class="bloom" role="img" aria-label="Soft grey flower illustration" style="left:70px; top:130px; width:440px; height:430px;"></div>
    <p class="centered tagline front-tagline">LOCAL • PURE • RAW</p>
    <div class="rule" style="left:57px; top:153px; width:296px;"></div>
    <h1 class="centered wordmark front-wordmark">HONEY</h1>
    <div class="rule" style="left:171px; top:315px; width:359px;"></div>
    <div class="brand-circle front-circle"></div>
    <p class="centered brand-name front-brand">Amber Hollow<br>Apiary</p>
    <p class="centered net-weight front-net">NET WT. 1 LB<br>(454 G)</p>
    <div class="ornament" role="img" aria-label="Scrolling corner ornament" style="left:68px; top:692px; width:160px; height:150px;"></div>
    <div class="ornament" role="img" aria-label="Scrolling corner ornament" style="left:359px; top:692px; width:150px; height:150px;"></div>
  </section>

  <section class="label label--back">
    <svg class="label-shape" viewBox="0 0 568 894" aria-hidden="true">
      <path d="M56,2 H512 L530,20 V131 H566 V752 H530 V874 L512,892 H56 L38,874 V752 H2 V131 H38 V20 Z" fill="var(--paper)" stroke="var(--ink)" stroke-width="1"/>
      <path d="M68,22 H500 L514,36 V146 H508 V340 M508,740 V862 L496,874 H72 L54,862 V740 M54,340 V146 H48 V36 Z" fill="none" stroke="var(--ink)" stroke-width="1.2"/>
    </svg>
    <div class="bloom" role="img" aria-label="Soft grey flower illustration" style="left:70px; top:130px; width:420px; height:300px;"></div>
    <div class="brand-circle back-circle"></div>
    <p class="brand-name back-brand">Amber Hollow<br>Apiary</p>
    <h2 class="wordmark back-wordmark">HONEY</h2>
    <p class="tagline back-tagline">LOCAL • PURE • RAW</p>
    <p class="centered promise">“AMBER HOLLOW APIARY PROMISES 100%<br>PURE HONEY, NEVER PASTEURIZED, AND<br>SOURCED EXCLUSIVELY FROM BEEHIVES<br>WE KEEP NEAR MAPLE FORK,<br>WEST VIRGINIA”</p>
    <h3 class="centered ingredients-title">INGREDIENTS</h3>
    <div class="nutrition">
      <p><strong class="lead">NUTRITION FACTS</strong> SERVINGS: 22, <strong>SERV. SIZE: 1 TBSP (21G),</strong></p>
      <p>AMOUNT PER SERVING: <strong>CALORIES <span class="big">60</span></strong>, <strong>TOTAL FAT</strong> 0G (0% DV), SAT.<br>FAT 0G (0% DV), TRANS FAT 0G, <strong>CHOLEST.</strong> 0MG (0% DV),<br><strong>SODIUM</strong> 0MG (0% DV), <strong>TOTAL CARB.</strong> 17G (6% DV), FIBER 0G (0% DV),<br>TOTAL SUGARS 17G (34% DV), <strong>PROTEIN 0G,</strong> VIT. D (0% DV),<br>CALCIUM (0% DV), IRON (0% DV), POTAS. (0% DV).</p>
      <p class="note">*ONE SERVING ADDS 17G OF SUGAR TO YOUR DIET AND<br>REPRESENTS 34% OF THE DAILY VALUE FOR ADDED SUGARS</p>
    </div>
    <p class="centered infant-warning">“DO NOT FEED HONEY TO INFANTS UNDER ONE YEAR OLD”</p>
    <address class="centered address">AMBER HOLLOW APIARY<br>118 LINDEN RIDGE ROAD<br>MAPLE FORK, WV 25000<br>WWW.AMBERHOLLOWAPIARY.CO</address>
    <p class="centered net-weight back-net">NET WT. 1 LB<br>(454 G)</p>
    <div class="ornament" role="img" aria-label="Scrolling corner ornament" style="left:66px; top:692px; width:100px; height:162px;"></div>
    <div class="ornament" role="img" aria-label="Scrolling corner ornament" style="left:357px; top:692px; width:145px; height:162px;"></div>
  </section>

</main>
</body>
</html>
```